make a fireworks website

we are manufacturer of fireworks in Asia.
we need a HD fireworks website for showing product to all world customers.
we also need an register for member system,location, forum,products..etc
I added my Logo for the company.
brightnova.com.hk

and please message me if you have
any question.
here some example of website:
http://www.skyplumeshow.com/
http://www.tornelupyro.com/
http://www.quarvel-pyro.co.uk/
http://www.mirethpyro.co.uk/

```html
<!DOCTYPE html>
<html lang="en">
<head>
<meta charset="utf-8">
<title>BrightNova – Fireworks Manufacturer</title>
<link rel="stylesheet" href="https://fonts.googleapis.com/css2?family=Archivo+Black&family=Arimo:wght@400;700&family=Anton&family=Lato:wght@300&display=swap">
<style>
  :root {
    --night: #000000;
    --sky-deep: #1d1a2b;
    --sky-mid: #3a2e4a;
    --glow: #c9a7e0;
    --nav-purple: #9c4aa1;
    --nav-dark: #6e3575;
    --nav-soft: #cda2d1;
    --promo-purple: #7a3a80;
    --flame: #ff7f27;
    --gold: #ffc20e;
    --stone: #7f7f7f;
    --panel: #303030;
    --panel-text: #c4c4c4;
    --white: #ffffff;
  }
  * { box-sizing: border-box; margin: 0; padding: 0; }
  html, body { width: 991px; height: 1200px; overflow: hidden; background: var(--night); }
  body { position: relative; font-family: "Arimo", Arial, sans-serif; }
  .abs { position: absolute; }

  .hero-photo {
    left: 0; top: 0; width: 991px; height: 498px;
    background:
      radial-gradient(ellipse 230px 210px at 270px 290px, rgba(230,200,240,.55), rgba(120,100,170,.25) 55%, transparent 80%),
      radial-gradient(ellipse 90px 70px at 210px 390px, rgba(255,220,170,.5), transparent 80%),
      linear-gradient(160deg, var(--sky-mid), var(--sky-deep) 60%, #241c2a);
  }

  .site-nav { left: 34px; top: 33px; width: 931px; height: 68px; }
  .brand-box {
    left: 53px; top: 52px; width: 92px; height: 47px; background: var(--white);
    display: flex; align-items: center; justify-content: center;
    font-family: "Arimo", Arial, sans-serif; font-weight: 700; font-size: 10px; color: var(--nav-dark);
  }
  .util-link { top: 41px; font-size: 16px; color: var(--nav-soft); display: flex; align-items: center; gap: 4px; }
  .util-dot { width: 20px; height: 20px; border-radius: 50%; background: var(--nav-dark); display: inline-block; position: relative; }
  .util-dot::after { content: ""; position: absolute; left: 7px; top: 7px; width: 6px; height: 6px; border-radius: 50%; background: var(--nav-soft); opacity: .6; }
  .search-box {
    left: 754px; top: 41px; width: 148px; height: 22px; border-radius: 11px;
    background: var(--nav-dark); color: var(--nav-soft); font-size: 16px; padding-left: 8px; line-height: 22px;
  }
  .search-go { left: 912px; top: 42px; }
  .main-link { top: 75px; font-size: 16px; font-weight: 700; color: var(--nav-dark); letter-spacing: .5px; }
  .main-link.is-active { color: var(--nav-soft); }

  .hero-promo { left: 498px; top: 150px; width: 493px; height: 302px; background: var(--promo-purple); border-radius: 151px 0 0 151px; }
  .photo-circle { border-radius: 50%; background: radial-gradient(circle at 45% 40%, #d9d3ee, #4a5fa8 35%, #1d2a5c 70%, #0c1230); }
  .hero-circle { left: 539px; top: 186px; width: 229px; height: 229px; }
  .promo-text { font-family: "Arimo", Arial, sans-serif; font-weight: 700; color: var(--flame); text-align: center; }
  .promo-small { font-size: 24px; letter-spacing: 1px; }
  .promo-big { font-size: 48px; letter-spacing: 2px; line-height: 1; }

  .welcome { left: 33px; top: 547px; font-family: "Archivo Black", "Arial Black", sans-serif; font-size: 44px; line-height: 68px; color: var(--stone); letter-spacing: 1px; -webkit-text-stroke: 1px #555; }
  .welcome-word { left: 560px; top: 540px; font-family: "Anton", Impact, sans-serif; font-size: 108px; line-height: 130px; color: var(--gold); transform: scaleX(.92); transform-origin: left top; }

  .topic { top: 717px; height: 161px; background: var(--panel); padding: 8px 13px; }
  .topic h2 { font-size: 20px; font-weight: 700; color: var(--white); margin-bottom: 18px; }
  .topic p { font-size: 15px; color: var(--panel-text); line-height: 18px; margin-bottom: 18px; }

  .product-promo { left: 0; top: 899px; width: 653px; height: 301px; background: var(--stone); border-radius: 0 150px 150px 0; }
  .product-circle { left: 383px; top: 936px; width: 229px; height: 229px; }
  .product-text { left: 37px; top: 936px; font-family: "Lato", sans-serif; font-weight: 300; font-size: 46px; line-height: 59px; color: var(--white); letter-spacing: 1px; }

  .side-heading { left: 683px; top: 893px; font-family: "Lato", sans-serif; font-weight: 300; font-size: 32px; line-height: 40px; color: var(--white); }
  .side-copy { left: 682px; top: 1008px; width: 309px; overflow: hidden; font-size: 15px; line-height: 18px; color: #e0e0e0; }
  .side-copy p { margin-bottom: 18px; width: 296px; }
</style>
</head>
<body>
  <div class="abs hero-photo" role="img" aria-label="Night sky with a large burst of fireworks"></div>

  <svg class="abs site-nav" viewBox="0 0 931 68" aria-hidden="true">
    <path d="M24 19 H270 L300 0 H907 A24 24 0 0 1 931 24 V44 A24 24 0 0 1 907 68 H24 A24 24 0 0 1 24 19 Z" fill="var(--nav-purple)"/>
  </svg>
  <div class="abs brand-box">brightnova.com.hk</div>

  <div class="abs util-link" style="left:493px"><span class="util-dot"></span>LOCATION</div>
  <div class="abs util-link" style="left:612px"><span class="util-dot"></span>PRODUCT</div>
  <div class="abs search-box">SEARCH</div>
  <svg class="abs search-go" width="20" height="18" viewBox="0 0 20 18" aria-hidden="true"><path d="M0 0 L20 9 L0 18 Z" fill="var(--nav-dark)"/></svg>

  <nav>
    <div class="abs main-link" style="left:435px">HOME</div>
    <div class="abs main-link" style="left:543px">PRODUCT</div>
    <div class="abs main-link is-active" style="left:689px">BRANCHES</div>
    <div class="abs main-link" style="left:847px">CONTACT</div>
  </nav>

  <section>
    <div class="abs hero-promo"></div>
    <div class="abs photo-circle hero-circle" role="img" aria-label="City skyline with a tower lit by fireworks at night"></div>
    <div class="abs promo-text promo-small" style="left:748px;top:170px">PROMOTIONAL</div>
    <div class="abs promo-text promo-big" style="left:782px;top:212px">TEXT</div>
    <div class="abs promo-text promo-big" style="left:797px;top:280px">FOR</div>
    <div class="abs promo-text promo-big" style="left:797px;top:348px">THE</div>
    <div class="abs promo-text promo-small" style="left:748px;top:407px">COMPANY</div>
  </section>

  <h1>
    <span class="abs welcome">WELCOME TO THE<br>GRAND RANGE OF</span>
    <span class="abs welcome-word">Fireworks</span>
  </h1>

  <section>
    <article class="abs topic" style="left:23px;width:299px">
      <h2>TOPIC 1</h2>
      <p>Text here. Text here. Text here. Text here. Text here. Text here. Text here. Text here.</p>
      <p>Text here. Text here. Text here.</p>
    </article>
    <article class="abs topic" style="left:342px;width:301px">
      <h2>TOPIC 2</h2>
      <p>Text here. Text here. Text here. Text here. Text here. Text here. Text here. Text here.</p>
      <p>Text here. Text here. Text here.</p>
    </article>
    <article class="abs topic" style="left:663px;width:297px">
      <h2>TOPIC 3</h2>
      <p>Text here. Text here. Text here. Text here. Text here. Text here. Text here. Text here.</p>
      <p>Text here. Text here. Text here.</p>
    </article>
  </section>

  <section>
    <div class="abs product-promo"></div>
    <div class="abs photo-circle product-circle" role="img" aria-label="City skyline with a tower lit by fireworks at night"></div>
    <div class="abs product-text">PROMOTIONAL<br>TEXT FOR<br>THIS<br>PRODUCT</div>
    <h2 class="abs side-heading">HEADER FOR THE<br>TEXT BELOW</h2>
    <div class="abs side-copy">
      <p>Some descriptive text here.Some descriptive text here.Some descriptive text here.Some descriptive text here.Some descriptive text here.</p>
      <p>Some descriptive text here.Some descriptive text here.Some descriptive text here.</p>
      <p>Some descriptive text here.</p>
    </div>
  </section>
</body>
</html>
```